Stationary for Keeping Steady

we are in the process of creating a more professional image for our company Keeping Steady Paramedical Services. We have recently had a new logo and general brochure designed using artpitchhub and have been impressed by the quality of submissions.

We need:
- Letterhead (A4)
- Business Cards
- With compliments slips
- Email stationary

Letterhead information:
Address - 47 Wattlebrook Drive, Fernhollow Vic 3091
Phone - 1800 462 817
email - enquiries@keepsteady.com.au
Internet - www.keepsteady.com.au
ABN - 82 463 915 207
ACN - 264 871 035

Files need to be able to be edited in Illustrator CS2

Business Cards / with compliments slips / email stationary:
Double sided.
One side to have Name, Mobile number, company phone 1800462817, email, internet address

Files need to be able to be edited in Illustrator CS2 (except email stationary)

Our website is www.keepsteady.com.au for more information. Do not base designs on the website as it will eventually be revised.

Target Market(s)

Australian based businesses, government departments and schools. We specialise in corporate customers rather than public first aid course

Industry/Entity Type

Internet

Requirements
Must have
• Where applicable file to be editable in illustrator CS2 to allow future alterations.

```html
<!DOCTYPE html>
<html lang="en">
<head>
<meta charset="utf-8">
<title>Keeping Steady Paramedical Services – Letterhead</title>
<link href="https://fonts.googleapis.com/css2?family=Questrial&family=Open+Sans:wght@600&display=swap" rel="stylesheet">
<style>
  :root {
    --red: #b8232b;
    --deep-red: #c0101a;
    --ink: #1a1716;
    --blush: #f3a9ab;
    --page-edge: #9a7b86;
    --white: #ffffff;
  }
  html, body {
    margin: 0;
    width: 1200px;
    height: 988px;
    overflow: hidden;
    background: var(--white);
  }
  .canvas {
    position: relative;
    width: 1200px;
    height: 988px;
    overflow: hidden;
  }
  .backdrop {
    position: absolute;
    inset: 0;
  }
  .letterhead {
    position: absolute;
    left: 498px;
    top: 60px;
    width: 595px;
    height: 841px;
    background: var(--white);
    border: 1px solid var(--page-edge);
    overflow: hidden;
  }
  .header-swoosh {
    position: absolute;
    left: 0;
    top: 0;
  }
  .brand-square {
    position: absolute;
    left: 80px;
    top: 14px;
    width: 58px;
    height: 58px;
    background: var(--red);
  }
  .brand-name {
    position: absolute;
    left: 200px;
    top: 8px;
    margin: 0;
    font-family: "Questrial", sans-serif;
    font-weight: 400;
    font-size: 40px;
    line-height: 48px;
    color: var(--red);
    letter-spacing: 0.5px;
  }
  .brand-tagline {
    position: absolute;
    left: 200px;
    top: 52px;
    margin: 0;
    font-family: "Questrial", sans-serif;
    font-size: 18.5px;
    line-height: 22px;
    color: var(--ink);
    letter-spacing: 0.3px;
  }
  .contact {
    position: absolute;
    left: 150px;
    top: 75px;
    width: 400px;
    margin: 0;
    font-family: "Open Sans", sans-serif;
    font-weight: 600;
    font-size: 10px;
    line-height: 12.5px;
    color: var(--ink);
    text-align: center;
  }
  .contact span + span { margin-left: 12px; }
  .footer-border {
    position: absolute;
    left: 0;
    bottom: 0;
    width: 595px;
    height: 56px;
    background: linear-gradient(90deg, var(--ink) 0%, var(--red) 25%, var(--ink) 50%, var(--red) 75%, var(--ink) 100%);
  }
</style>
</head>
<body>
<div class="canvas">
  <svg class="backdrop" width="1200" height="988" viewBox="0 0 1200 988" aria-hidden="true">
    <defs>
      <linearGradient id="blush-fade" x1="0" y1="0" x2="1" y2="0">
        <stop offset="0" stop-color="#ffffff"/>
        <stop offset="0.3" stop-color="#f3a9ab"/>
        <stop offset="0.7" stop-color="#f3a9ab"/>
        <stop offset="1" stop-color="#ffffff"/>
      </linearGradient>
    </defs>
    <ellipse cx="800" cy="480" rx="580" ry="190" transform="rotate(-55 800 480)" fill="url(#blush-fade)"/>
  </svg>

  <main class="letterhead">
    <svg class="header-swoosh" width="595" height="160" viewBox="0 0 595 160" aria-hidden="true">
      <path d="M46 30 C0 40 -10 80 40 100 C130 140 300 150 380 148 C470 145 560 125 593 115 C540 125 430 136 350 134 C230 130 80 110 20 80 C5 60 20 40 46 30 Z" fill="var(--ink)"/>
      <path d="M46 30 C10 42 5 70 45 88 C130 118 300 130 380 128 C470 125 560 118 593 115 C530 122 430 128 350 125 C230 120 70 100 22 75 C12 55 25 40 46 30 Z" fill="var(--deep-red)"/>
    </svg>

    <div class="brand-square"></div>
    <h1 class="brand-name">Keeping Steady</h1>
    <p class="brand-tagline">Paramedical Services Pty Ltd</p>
    <p class="contact">
      <span>Phone - 1800 462 817</span><span>ABN - 82 463 915 207</span><span>ACN - 264 871 035</span><br>
      email - enquiries@keepsteady.com.au - www.keepsteady.com.au<br>
      Address - 47 Wattlebrook Drive, Fernhollow Vic 3091
    </p>

    <div class="footer-border" role="img" aria-label="Decorative footer border of ribbon waves with repeated brand crosses"></div>
  </main>
</div>
</body>
</html>
```